Solvane Vitality MediSpa Brochure

We need a new brochure design. The old is attached.

We are wanting a three panel brochure for med spa designed and ready for print. The brochure will have content and images on both sides. We attached the old brochure in pdf format. The content needs to stay as on the attached pdf but please feel free to offer new designs. The color needs to match the attached logo, which is a light blue and teal. All images we want on the brochure are also attached.

The design must have an 1/8 in space from each edge for printing purposes

Target Market(s)

Men and Women

Industry/Entity Type

Wellness

Font styles to use
Sans Serif

Colors
34a6d7
33b8a4

Requirements
Must have
• soft curves. must have a 1/8 in space on all edges (including interior) to give bleed space for printing. Use content written on attached brochure.

```html
<!DOCTYPE html>
<html lang="en">
<head>
<meta charset="utf-8">
<title>Solvane Vitality MediSpa Brochure</title>
<link href="https://fonts.googleapis.com/css2?family=Open+Sans:wght@400;600;700;800&family=Montserrat:wght@400;600;700&display=swap" rel="stylesheet">
<style>
:root{
  --teal:#33b8a4;
  --blue:#34a6d7;
  --deep:#1f8f9a;
  --ink:#3b4b55;
  --soft:#e6f5f6;
  --paper:#ffffff;
  --bg:#eef1f3;
}
*{box-sizing:border-box;margin:0;padding:0}
html,body{width:849px;height:1200px;overflow:hidden;background:var(--bg);font-family:"Open Sans",Arial,sans-serif;color:var(--ink)}
.canvas{position:relative;width:849px;height:1200px}
.sheet{position:absolute;left:20px;width:809px;height:540px;background:var(--paper);display:flex;box-shadow:0 4px 14px rgba(0,0,0,.18);overflow:hidden}
.sheet--outside{top:40px}
.sheet--inside{top:620px}
.panel{position:relative;width:269.67px;height:100%;padding:18px;overflow:hidden}
.panel+.panel{border-left:1px solid #d9e6e8}
.wave{position:absolute;left:0;width:100%;pointer-events:none}
.wave--bottom{bottom:0;height:110px}
.wave--top{top:0;height:120px}
.photo{background:linear-gradient(135deg,#bfe6f0,#7cc7d8 60%,#4fb3b4);}
.photo--soft{background:linear-gradient(160deg,#d6eff7,#a9dcea 55%,#7fcabf)}
.brand{display:flex;align-items:center;gap:8px;font-family:"Montserrat",sans-serif;font-weight:700;color:var(--deep);font-size:15px;line-height:1.1}
.brand__dot{width:14px;height:14px;border-radius:50%;background:var(--teal);flex:none}
.tag{display:inline-block;background:var(--teal);color:#fff;font-weight:700;font-size:10px;text-transform:uppercase;padding:4px 8px;border-radius:0 10px 10px 0;margin:10px 0 5px -18px;padding-left:18px}
.tag--blue{background:var(--blue)}
.body{font-size:7.5px;line-height:1.45;color:var(--ink)}
.list{list-style:none;font-size:10px;font-weight:700;color:var(--deep);margin-top:4px}
.list li{padding-left:14px;position:relative;margin:3px 0}
.list li::before{content:"";position:absolute;left:0;top:3px;width:7px;height:7px;border-radius:50%;background:var(--blue)}
.learn{position:absolute;left:18px;right:18px;bottom:36px;color:#fff;z-index:2}
.learn__title{font-family:"Montserrat",sans-serif;font-weight:700;font-size:14px}
.learn__url{font-size:9px}
.contact{font-family:"Montserrat",sans-serif;font-weight:700;color:var(--deep);font-size:15px;line-height:1.4}
.address{font-size:8px;line-height:1.4;color:var(--ink);margin-top:6px}
.cta{background:var(--teal);color:#fff;font-weight:700;font-size:11px;padding:6px 10px;border-radius:12px 0 0 12px;text-align:center;margin-right:-18px}
.cta strong{display:block;font-size:13px}
.audience{font-family:"Montserrat",sans-serif;font-weight:700;color:#fff;font-size:12px;text-transform:uppercase;background:var(--blue);display:inline-block;padding:4px 10px;border-radius:10px}
.heading{font-family:"Montserrat",sans-serif;font-weight:700;text-transform:uppercase;font-size:16px;line-height:1.1}
.heading--laser{position:relative;z-index:2;color:#fff;margin:2px 0 62px}
.sub{font-weight:700;font-size:9px;color:var(--deep);margin-top:8px}
.cols{display:flex;gap:10px}
.cols .list{flex:1;font-size:9px}
</style>
</head>
<body>
<main class="canvas">

  <section class="sheet sheet--outside">
    <article class="panel panel--info">
      <span class="tag">Solvane's Promise &amp; Wellness</span>
      <p class="body">We combine medical expertise with a calm spa setting so every guest leaves feeling refreshed, confident and cared for. Each plan is built around your goals and your skin.</p>
      <span class="tag tag--blue">Why choose our wellness team?</span>
      <p class="body">Licensed providers, modern equipment and honest advice. We listen first, explain every option clearly and follow up after each visit to keep results lasting.</p>
      <span class="tag">Exclusive Memberships</span>
      <p class="body">Save on treatments all year with a plan that suits you.</p>
      <ul class="list">
        <li>SILVER Membership</li>
        <li>GOLD Membership</li>
        <li>PLATINUM Membership</li>
      </ul>
      <svg class="wave wave--bottom" viewBox="0 0 270 110" preserveAspectRatio="none" aria-hidden="true">
        <path d="M0 30 C80 0 170 60 270 20 L270 110 L0 110Z" fill="var(--blue)" opacity=".5"/>
        <path d="M0 45 C90 20 170 70 270 35 L270 110 L0 110Z" fill="var(--teal)"/>
      </svg>
      <div class="learn">
        <div class="learn__title">Learn More At</div>
        <div class="learn__url">www.solvanevitality.example</div>
      </div>
    </article>

    <article class="panel panel--back">
      <div class="photo" role="img" aria-label="Portrait photo of the spa's medical director" style="height:120px;border-radius:6px"></div>
      <p class="body" style="margin-top:8px">Our director leads a caring team devoted to safe, natural-looking results.</p>
      <div style="position:absolute;left:18px;right:18px;top:250px">
        <div class="brand"><span class="brand__dot"></span>Solvane Vitality MediSpa</div>
        <p class="address">218 Harborline Ave, Suite 100<br>Brookvale</p>
        <p class="sub">Schedule a Consultation</p>
      </div>
      <svg class="wave wave--bottom" viewBox="0 0 270 110" preserveAspectRatio="none" aria-hidden="true">
        <path d="M0 40 C90 10 180 70 270 30 L270 110 L0 110Z" fill="var(--teal)" opacity=".35"/>
        <path d="M0 60 C100 35 180 85 270 50 L270 110 L0 110Z" fill="var(--teal)"/>
      </svg>
      <div style="position:absolute;left:18px;bottom:118px;z-index:2" class="contact">
        Ph: (555) 410-2270<br>Fax: (555) 410-2281
      </div>
    </article>

    <article class="panel panel--cover" style="background:var(--soft)">
      <div class="brand" style="justify-content:center;margin-top:6px"><span class="brand__dot"></span>Solvane Vitality MediSpa</div>
      <div class="photo" role="img" aria-label="Close-up photo of a woman with glowing skin" style="height:220px;margin:16px -18px 0 30px;border-radius:110px 0 0 110px"></div>
      <div class="cta" style="margin-top:14px">CALL US NOW<strong>(555) 410-2270</strong></div>
      <svg class="wave wave--bottom" viewBox="0 0 270 110" preserveAspectRatio="none" aria-hidden="true">
        <path d="M0 30 C90 0 180 60 270 20 L270 110 L0 110Z" fill="var(--blue)" opacity=".45"/>
        <path d="M0 50 C100 25 180 80 270 40 L270 110 L0 110Z" fill="var(--teal)"/>
      </svg>
      <div style="position:absolute;left:0;right:0;bottom:110px;text-align:center;z-index:2"><span class="audience">For Women and Men</span></div>
    </article>
  </section>

  <section class="sheet sheet--inside">
    <article class="panel panel--laser">
      <svg class="wave wave--top" viewBox="0 0 270 120" preserveAspectRatio="none" aria-hidden="true">
        <path d="M0 0 L270 0 L270 70 C180 105 90 55 0 95Z" fill="var(--teal)"/>
      </svg>
      <h2 class="heading heading--laser">Laser<br>Treatments</h2>
      <span class="tag">Laser Hair Removal</span>
      <p class="body">Smooth, lasting results for face and body with gentle, fast sessions suited to most skin types.</p>
      <span class="tag tag--blue">CO2 Resurfacing</span>
      <p class="body">Fractional laser renews texture, softens fine lines and evens tone with minimal downtime.</p>
      <span class="tag">IPL Photofacial</span>
      <p class="body">Light therapy fades sun spots and redness, revealing a brighter, clearer complexion.</p>
      <span class="tag tag--blue">IPL Acne / Rosacea / Spider Veins</span>
      <p class="body">Targeted pulses calm breakouts, reduce flushing and clear small visible veins.</p>
    </article>

    <article class="panel panel--injectables">
      <div class="photo photo--soft" role="img" aria-label="Photo of a smiling woman in a sun hat outdoors" style="height:230px;margin:-18px -18px 0"></div>
      <span class="tag">Injectables</span>
      <div class="cols">
        <ul class="list"><li>Relaxa</li><li>Contoura</li><li>Smoothin</li></ul>
        <ul class="list"><li>Lumafill</li><li>Plumelle</li><li>Hydrafill</li></ul>
        <ul class="list"><li>Firmacol</li><li>Liftiva</li><li>Volara</li></ul>
      </div>
      <span class="tag tag--blue">Laser Tattoo Removal</span>
      <p class="body">Safe, stepwise fading of unwanted ink with comfort-focused care.</p>
      <svg class="wave wave--bottom" viewBox="0 0 270 110" preserveAspectRatio="none" aria-hidden="true" style="height:60px">
        <path d="M0 40 C90 10 180 60 270 25 L270 110 L0 110Z" fill="var(--teal)"/>
      </svg>
    </article>

    <article class="panel panel--skincare">
      <span class="tag">Body &amp; Wellness</span>
      <p class="body">Body contouring, skin tightening and vitamin therapy to help you look and feel your best.</p>
      <span class="tag tag--blue">Wellness Programs</span>
      <p class="body">Weight care, hormone balance and nutrition coaching guided by our medical staff.</p>
      <div style="background:var(--teal);color:#fff;font-family:'Montserrat',sans-serif;font-weight:700;font-size:13px;padding:8px 12px;margin:14px -18px 0;border-radius:0 0 0 20px">Skincare &amp; Skin Cosmetics</div>
      <div style="margin-top:40px">
        <div class="brand"><span class="brand__dot"></span>Solvane Vitality MediSpa</div>
        <p class="address">218 Harborline Ave, Suite 100<br>Brookvale</p>
        <div class="contact" style="margin-top:8px">Ph: (555) 410-2270<br>Fax: (555) 410-2281</div>
        <p class="address">www.solvanevitality.example</p>
      </div>
      <svg class="wave wave--bottom" viewBox="0 0 270 110" preserveAspectRatio="none" aria-hidden="true" style="height:60px">
        <path d="M0 30 C90 0 180 55 270 20 L270 110 L0 110Z" fill="var(--blue)"/>
      </svg>
    </article>
  </section>

</main>
</body>
</html>
```